Web Design Project for velbrook

We are looking for a sleek and sophisticated website design for our already developed web-based gallery management software application. Here is a link to our web-app: http://www.vel-brook.co

You will login on the main page and then we would like to include all of the information on the PDF that I am providing below (it outlines what?, where?, why? who? and how much?). Basically, we need a home page, about page, and a pricing page, as well as a sign up page that should be navigable from the upper right hand corner of the site where the sign in/sign up would be located. Also, our 3 tenets are that the software program is "attractive, accessible, and affordable", which might need to be somehow incorporated. There are a few websites that we would like for you to take inspiration from listed below:

https://tidemoxen.com (for homepage)
https://plumwovenly.com (for homepage/pricing page/etc)
https://tidemoxen.com/tour (for a tour of how the product works)

We are currently having a logo designed and will share that as soon as it is available! Also, let us know if you need photos/screen shots, as we can provide them.

Thanks!

Reason: Extending deadline as we are just now getting designs we would like to see fully developed.

Target Market(s)

art galleries, artists, art collectors, art consultants, museums

Industry/Entity Type

Software

Requirements
Must have
• Home page
About page (or tour through the app)
Pricing page
Sign up page (the more click-throughs to signing up the better)

```html
<!DOCTYPE html>
<html lang="en">
<head>
<meta charset="utf-8">
<title>velbrook – Pricing</title>
<link rel="stylesheet" href="https://fonts.googleapis.com/css2?family=Montserrat:wght@500;600;700&family=Mulish:wght@400;500&family=Open+Sans:wght@700&family=Raleway:wght@300;400;500&display=swap">
<style>
:root{
  --brand:#27a9e1;
  --brand-dark:#1497d0;
  --orange:#f7941d;
  --ink:#2b2b2b;
  --body:#4a4a4a;
  --line:#dcdcdc;
  --panel:#f5f5f5;
  --band-top:#7fd5f3;
  --band-bottom:#4dbfea;
  --tag-blue:#29abe2;
  --tag-navy:#1479c7;
  --footer:#88d3ed;
  --footer-ink:#1f6f96;
  --white:#ffffff;
}
*{box-sizing:border-box;margin:0;padding:0}
html,body{width:1099px;height:1200px;overflow:hidden;background:var(--white)}
body{position:relative;font-family:"Mulish",Arial,sans-serif;color:var(--body)}

.site-header{position:absolute;left:0;top:0;width:1099px;height:75px;background:linear-gradient(#ffffff,#ebebeb);border-bottom:1px solid #d6d6d6}
.brand{position:absolute;left:129px;top:22px;display:flex;align-items:center;gap:8px;font-family:"Raleway",sans-serif;font-weight:400;font-size:27px;color:var(--brand);text-decoration:none}
.brand-dot{width:26px;height:26px;border:3px solid var(--brand);border-radius:50%}
.main-nav{position:absolute;left:346px;top:34px;display:flex;gap:22px;list-style:none}
.main-nav a{font-family:"Raleway",sans-serif;font-weight:500;font-size:12.5px;color:#777;text-decoration:none;letter-spacing:.2px}
.main-nav a.is-current{color:var(--brand)}
.account-actions{position:absolute;left:804px;top:24px;display:flex;gap:9px}
.btn-account{display:block;width:79px;height:31px;line-height:31px;text-align:center;border-radius:4px;font-family:"Open Sans",sans-serif;font-weight:700;font-size:14px;letter-spacing:1px;color:var(--white);text-decoration:none}
.btn-signin{background:var(--orange)}
.btn-signup{background:var(--brand-dark)}

.page-banner{position:absolute;left:0;top:76px;width:1099px;height:118px;background:linear-gradient(var(--band-top),var(--band-bottom))}
.banner-scene{position:absolute;left:0;top:0;width:1099px;height:118px;background:linear-gradient(100deg,#7ad3f2 0%,#86d8f4 45%,#5cc6ee 100%)}
.page-banner h1{position:absolute;left:129px;top:26px;font-family:"Raleway",sans-serif;font-weight:300;font-size:45px;color:var(--white)}

.plan-card{position:absolute;left:129px;width:841px;height:349px;border:1px solid var(--line);border-radius:4px;overflow:hidden;background:var(--white)}
.plan-card.activation{top:239px}
.plan-card.maintenance{top:614px}
.plan-intro{height:134px;background:var(--panel);padding:22px 26px 0}
.plan-intro h2{font-family:"Montserrat",sans-serif;font-weight:600;font-size:21px;color:var(--ink);letter-spacing:.2px}
.plan-intro p{margin-top:11px;font-size:13.3px;line-height:22px;letter-spacing:-.15px;color:var(--body)}
.feature-list{position:absolute;left:26px;top:149px;width:420px;list-style:none}
.feature-list li{position:relative;padding-left:15px;font-size:14px;line-height:14px;margin-bottom:13.5px;color:var(--body)}
.feature-list li::before{content:"";position:absolute;left:1px;top:3px;width:5px;height:5px;border-top:2px solid var(--brand);border-right:2px solid var(--brand);transform:rotate(45deg)}

.price-tag{position:absolute;left:528px;top:112px;width:202px}
.tag-cord{display:block}
.tag-card{margin-top:-6px;border:1px solid #cfcfcf;border-radius:3px;background:var(--white);box-shadow:0 4px 5px rgba(0,0,0,.18);overflow:hidden}
.tag-label{height:50px;padding:6px 12px 0;background:linear-gradient(#ffffff,#eeeeee);font-family:"Montserrat",sans-serif;font-weight:700;font-size:17.5px;line-height:20px;color:#111}
.tag-amount{position:relative;height:56px;margin:0 2px 2px;background:var(--tag-blue);display:flex;align-items:center;padding-left:10px;font-family:"Montserrat",sans-serif;font-weight:700;color:var(--white)}
.tag-amount.navy{background:var(--tag-navy)}
.tag-amount .figure{font-size:44px;line-height:1}
.tag-amount .currency{font-size:18px;align-self:flex-start;margin:8px 0 0 4px}
.tag-amount svg{position:absolute;right:10px;top:6px}
.btn-plan{display:block;margin-top:7px;height:49px;line-height:49px;text-align:center;border-radius:4px;background:var(--brand-dark);font-family:"Montserrat",sans-serif;font-weight:600;font-size:21px;color:var(--white);text-decoration:none}

.like-widget{position:absolute;left:475px;top:1006px;display:flex;align-items:center;gap:6px;font-family:Arial,sans-serif;font-size:10px;color:#333}
.like-btn{display:flex;align-items:center;gap:3px;height:20px;padding:0 5px;border:1px solid #b6c1d6;border-radius:2px;background:#eef1f7;color:#3b5998;font-weight:700}
.like-square{width:10px;height:10px;background:#3b5998;border-radius:1px}

.site-footer{position:absolute;left:0;top:1049px;width:1099px;height:151px;background:var(--footer)}
.footer-nav{position:absolute;left:0;top:24px;width:1099px;display:flex;justify-content:center;align-items:center;gap:24px;list-style:none}
.footer-nav a{font-family:"Mulish",sans-serif;font-size:13.5px;color:var(--footer-ink);text-decoration:none;letter-spacing:.2px}
.social{display:flex;align-items:center;gap:5px}
.social-circle{width:28px;height:28px;border:2px solid var(--footer-ink);border-radius:50%}
.footer-brand{position:absolute;left:0;top:71px;width:1099px;text-align:center;font-family:"Raleway",sans-serif;font-weight:400;font-size:26px;color:var(--footer-ink)}
.copyright{position:absolute;left:0;top:115px;width:1099px;text-align:center;font-size:13.5px;color:var(--footer-ink);letter-spacing:.3px}
</style>
</head>
<body>

<header class="site-header">
  <a class="brand" href="http://www.vel-brook.co"><span class="brand-dot"></span>velbrook</a>
  <ul class="main-nav">
    <li><a href="#">HOME</a></li>
    <li><a href="#">ABOUT</a></li>
    <li><a href="#" class="is-current">PRICING</a></li>
    <li><a href="#">CONTAC US</a></li>
  </ul>
  <div class="account-actions">
    <a class="btn-account btn-signin" href="#">SIGN IN</a>
    <a class="btn-account btn-signup" href="#">SIGN UP</a>
  </div>
</header>

<section class="page-banner">
  <div class="banner-scene" role="img" aria-label="Sky-blue banner illustration with white clouds and flying birds"></div>
  <h1>Pricing</h1>
</section>

<article class="plan-card activation">
  <div class="plan-intro">
    <h2>ACTIVATION PLAN</h2>
    <p>Lorem Ipsum. Proin gravida nibh vel velit auctor aliquet. Aenean sollicitudin, lorem quis bibendum auctor, nisi elit consequat ipsum,<br>nec sagittis sem nibh id elit. Duis sed odio sit amet nibh vulputate cursus a sit amet mauris.</p>
  </div>
  <ul class="feature-list">
    <li>Lorem ipsum dolor sit amet, consectetur adipiscing elit.</li>
    <li>Ut eu mauris ac libero pharetra gravida.</li>
    <li>Nullam aliquet tortor ut nunc vulputate, sit amet tempus ligula vulputate.</li>
    <li>Integer nec sapien sed magna vestibulum hendrerit a et velit.</li>
    <li>Morbi in odio ac mi euismod sollicitudin.</li>
    <li>Vivamus interdum erat ac rhoncus vehicula.</li>
  </ul>
  <div class="price-tag">
    <svg class="tag-cord" width="202" height="56" viewBox="0 0 202 56">
      <path d="M101 10 L22 54 M101 10 L180 54" stroke="#9a9a9a" stroke-width="3" fill="none"/>
      <circle cx="101" cy="10" r="7" fill="#eeeeee" stroke="#a5a5a5" stroke-width="2"/>
    </svg>
    <div class="tag-card">
      <div class="tag-label">Activation<br>Fee</div>
      <div class="tag-amount"><span class="figure">500</span><span class="currency">$</span>
        <svg width="54" height="44" viewBox="0 0 54 44"><path d="M6 24 L20 38 L48 6" stroke="#d9e4ea" stroke-width="9" fill="none" stroke-linecap="round" stroke-linejoin="round"/></svg>
      </div>
    </div>
    <a class="btn-plan" href="#">Sign Up</a>
  </div>
</article>

<article class="plan-card maintenance">
  <div class="plan-intro">
    <h2>MONTHLY MAINTENANCE PLANS</h2>
    <p>Lorem Ipsum. Proin gravida nibh vel velit auctor aliquet. Aenean sollicitudin, lorem quis bibendum auctor, nisi elit consequat ipsum,<br>nec sagittis sem nibh id elit. Duis sed odio sit amet nibh vulputate cursus a sit amet mauris.</p>
  </div>
  <ul class="feature-list">
    <li>Lorem ipsum dolor sit amet, consectetur adipiscing elit.</li>
    <li>Ut eu mauris ac libero pharetra gravida.</li>
    <li>Nullam aliquet tortor ut nunc vulputate, sit amet tempus ligula vulputate.</li>
    <li>Integer nec sapien sed magna vestibulum hendrerit a et velit.</li>
    <li>Morbi in odio ac mi euismod sollicitudin.</li>
    <li>Vivamus interdum erat ac rhoncus vehicula.</li>
  </ul>
  <div class="price-tag">
    <svg class="tag-cord" width="202" height="56" viewBox="0 0 202 56">
      <path d="M101 10 L22 54 M101 10 L180 54" stroke="#9a9a9a" stroke-width="3" fill="none"/>
      <circle cx="101" cy="10" r="7" fill="#eeeeee" stroke="#a5a5a5" stroke-width="2"/>
    </svg>
    <div class="tag-card">
      <div class="tag-label">Monthly<br>Maintenance Fee</div>
      <div class="tag-amount navy"><span class="figure">100</span><span class="currency">$</span>
        <svg width="40" height="44" viewBox="0 0 40 44">
          <rect x="2" y="6" width="36" height="36" rx="3" fill="#e7eef3"/>
          <rect x="2" y="6" width="36" height="8" fill="#c9d6df"/>
          <rect x="9" y="1" width="4" height="9" rx="1" fill="#e7eef3"/>
          <rect x="27" y="1" width="4" height="9" rx="1" fill="#e7eef3"/>
          <g fill="#1479c7">
            <rect x="7" y="18" width="6" height="5"/><rect x="17" y="18" width="6" height="5"/><rect x="27" y="18" width="6" height="5"/>
            <rect x="7" y="26" width="6" height="5"/><rect x="17" y="26" width="6" height="5"/><rect x="27" y="26" width="6" height="5"/>
            <rect x="7" y="34" width="6" height="5"/><rect x="17" y="34" width="6" height="5"/><rect x="27" y="34" width="6" height="5"/>
          </g>
        </svg>
      </div>
    </div>
    <a class="btn-plan" href="#">Sign Up</a>
  </div>
</article>

<div class="like-widget">
  <span class="like-btn">Like</span>
  <span class="like-square"></span>
  <span>8,165 people like this.</span>
</div>

<footer class="site-footer">
  <ul class="footer-nav">
    <li><a href="#">HOME</a></li>
    <li><a href="#">ABOUT</a></li>
    <li><a href="#">PRICING</a></li>
    <li><a href="#">CONTAC US</a></li>
    <li><a href="#">PRIVACY POLICY</a></li>
    <li><a href="#">TERMS OF SERVICE</a></li>
    <li><a class="social" href="#"><span class="social-circle"></span>Friendsy</a></li>
    <li><a class="social" href="#"><span class="social-circle"></span>Chatterly</a></li>
  </ul>
  <div class="footer-brand">velbrook</div>
  <p class="copyright">© 2013 VELBROOK. ALL RIGHTS RESERVED.</p>
</footer>

</body>
</html>
```